Brochure flyer for handout and web distribution - 11 X 17 folded four pages 8.5 X 11

We need a brochure for trade shows. Title page is "When Speed To Market Counts - We Deliver"- company logos on bottom of the page.

We build cannabis grow facilities and can build 3-6 months faster than conventional building methods. We want to use green as a focus color. We have an image cannabis interactive that we want to have in the center fold. It comes from this webpage which has the building descriptions - https://www.tallowfen.com/cannabis-buildings

Also attached is an ad from Hempvora we did for a previous show that shows how I would like logos on the back cover - without the background image and without the text - replace text on back page with file attached with key advantages that we would like on the back page as well.

There are also some images from our partner MeltaBrook that we would love to show on the inside cover as well - so one page is Brevik interactive and buildings and the other inside page features MeltaBrook.

For content on Melta-Brook - When choosing between modular construction and traditionally constructed rooms, consider that all modular construction is objectively faster and more affordable. On average you can cut construction time by half when using a modular room and building design compared to conventionally construction. All components used to construct modular rooms and buildings have already been designed and fabricated at our plant, causing:
• Less disruption to your daily business operations
• Less construction waste and debris
Logos are attached for the back page - these can also be used on the front page. Website is www.rivenstalkworks.com (visit us). Contact us at info@rivenstalkworks.com

All images can be provided EPS - final design will need to be 300DPI minimum

Target Market(s)

Lead investors in Cannabis

Industry/Entity Type

Cannabis Industry

Font styles to use
Serif

Colors
0094D4
00A9DD
6FCCEA
C7EBF8
E9F6FB
00AB8E
00BBA5
67D7C9
C6EFE9
E9F9F6

Requirements
Must have
• Logos, website, 4 pages
Should not have
• Cannabis images

```html
<!DOCTYPE html>
<html lang="en">
<head>
<meta charset="utf-8">
<title>Brochure – When Speed To Market Counts</title>
<link rel="stylesheet" href="https://fonts.googleapis.com/css2?family=Bebas+Neue&family=Open+Sans:wght@400;600;700&display=swap">
<style>
:root{
  --bg:#d4d5d7;
  --paper:#ffffff;
  --green:#7cc242;
  --green-dark:#5fa52f;
  --teal:#1fa58c;
  --teal-deep:#16606b;
  --teal-mid:#2a9a90;
  --slate:#3d4049;
  --ink:#2b2b2b;
  --muted:#555a60;
  --head:"Bebas Neue", "Oswald", sans-serif;
  --body:"Open Sans", Arial, sans-serif;
}
*{margin:0;padding:0;box-sizing:border-box}
html,body{width:948px;height:1200px;overflow:hidden;background:var(--bg)}
body{position:relative;font-family:var(--body);color:var(--ink)}
.spread{position:absolute;left:98px;width:745px;height:481px;background:var(--paper);overflow:hidden}
.spread--outer{top:73px}
.spread--inner{top:614px}
.abs{position:absolute}
.fold{position:absolute;top:0;bottom:0;left:372px;width:1px;background:rgba(0,0,0,.08);z-index:5}

/* back cover */
.benefits{left:14px;top:24px;width:164px}
.benefits__title{font-family:var(--head);color:var(--green);font-size:14.5px;line-height:16.5px;letter-spacing:.2px}
.benefits__lead{font-size:6.6px;font-weight:600;line-height:9.3px;margin-top:4px;text-align:justify}
.benefit{position:relative;padding-left:17px;margin-top:7px}
.benefit__icon{position:absolute;left:0;top:1px;width:13px;height:13px;border-radius:50%;background:var(--green);border:1.5px solid #cfe9b8}
.benefit__name{font-size:6.4px;font-weight:700;line-height:8.4px}
.benefit__text{font-size:6.1px;line-height:8.4px;text-align:justify}

/* cover */
.cover-top{left:187px;top:0;width:558px;height:125px;background:linear-gradient(120deg,#23a88a 0%,#1d8c84 45%,#166170 100%)}
.cover-bar{left:397px;top:112px;width:348px;height:13px;background:var(--green);clip-path:polygon(3% 0,100% 0,100% 100%,0 100%)}
.cover-title{left:372px;top:32px;width:373px;text-align:center;font-family:var(--head);color:#fff;font-size:27px;line-height:34px;letter-spacing:.3px}
.cover-photo{left:187px;top:125px;width:558px;height:237px;background:linear-gradient(180deg,#c8ced3 0%,#e3e6e8 35%,#b9bfc4 62%,#a29e98 100%)}
.cover-strip{left:187px;top:362px;width:347px;height:10px;background:var(--green);clip-path:polygon(0 0,100% 0,95% 100%,0 100%)}
.cover-base{left:187px;top:372px;width:558px;height:109px;background:var(--slate)}
.contact{left:203px;top:410px;color:#fff}
.contact__title{font-family:var(--head);font-size:15px;letter-spacing:.3px}
.contact__line{font-size:6.6px;font-weight:700;margin-top:3px;display:flex;align-items:center;gap:4px}
.contact__dot{width:6px;height:6px;border-radius:50%;background:var(--green)}
.partners{left:390px;top:387px;display:flex;gap:7px}
.partner{width:79px;height:63px;background:#fff;border-radius:5px;display:flex;align-items:center;justify-content:center;gap:4px;font-size:7.4px;font-weight:700;color:var(--teal-deep);text-align:center;padding:0 4px}
.partner__mark{width:9px;height:9px;border-radius:50%;background:var(--green);flex:none}
.cover-url{left:390px;top:461px;width:337px;text-align:center;font-size:6.4px;font-weight:700;color:var(--green)}

/* inner left */
.campus{left:0;top:0;width:372px;height:184px;background:linear-gradient(170deg,#3d6d3a 0%,#5d8b44 40%,#8c9c86 60%,#4e7a39 100%)}
.campus-corner{left:0;top:0;width:90px;height:120px;background:var(--teal);clip-path:polygon(0 0,100% 0,0 100%);opacity:.85}
.buildings{left:11px;top:198px;width:341px}
.buildings__title{font-family:var(--head);color:var(--green);font-size:15px;line-height:17px;letter-spacing:.2px}
.buildings__lead{font-size:5.9px;font-weight:700;line-height:8.8px;margin-top:2px;width:341px;color:#3a3a3a;text-align:justify}
.bitem{position:relative;padding-left:13px;margin-top:4px;width:208px}
.bitem--wide{width:341px}
.bitem__num{position:absolute;left:0;top:0;width:9px;height:9px;border-radius:50%;background:var(--green);color:#fff;font-size:5.4px;font-weight:700;text-align:center;line-height:9px}
.bitem__name{font-size:6.1px;font-weight:700;line-height:8px;color:#333}
.bitem__text{font-size:5.5px;line-height:8px;color:#555}
.floorplan{left:230px;top:382px;width:118px;height:55px;background:linear-gradient(135deg,#d9ddd9,#9fb49a);transform:skewY(-20deg)}

/* inner right */
.features-bg{left:372px;top:0;width:373px;height:260px;background:linear-gradient(180deg,#1c9a86 0%,#2aa893 55%,rgba(42,168,147,.2) 85%,rgba(255,255,255,0) 100%)}
.features-title{left:372px;top:44px;width:373px;text-align:center;font-family:var(--head);color:#fff;font-size:16px;letter-spacing:.3px}
.features-lead{left:392px;top:80px;width:334px;text-align:center;color:#fff;font-size:5.9px;line-height:8.8px}
.tile{position:absolute;width:109px;height:72px;border:1px solid #fff}
.tile--light{background:linear-gradient(160deg,#f4f4f4,#d8d8d8)}
.tile--room{background:linear-gradient(180deg,#cfc7a7,#7c7a55)}
.tile--sky{background:linear-gradient(180deg,#5d8fc4 0%,#b9cde2 60%,#a9a68f 100%)}
.tile--rows{background:linear-gradient(90deg,#6b7a4e,#a7ac8a,#6b7a4e)}
.modular{left:388px;top:300px;width:342px;font-size:6.1px;line-height:9px;color:#555}
.modular p+p{margin-top:8px}
.perk{left:389px;display:flex;align-items:center;gap:6px;font-size:7.6px;font-weight:700;color:#444;line-height:9px}
.perk__icon{width:18px;height:18px;border-radius:50%;background:var(--slate);border:2px solid #d9dcdf;flex:none}
.wedge{left:564px;top:373px;width:181px;height:108px;background:var(--slate);clip-path:polygon(100% 0,100% 100%,0 100%)}
.base-line{left:0;top:470px;width:745px;height:4px;background:var(--green)}
</style>
</head>
<body>

<section class="spread spread--outer">
  <div class="abs benefits">
    <h2 class="benefits__title">Craft Growth Model<br>Advantages and Benefits</h2>
    <p class="benefits__lead">Our cultivators enjoy several distinct advantages and benefits compared to conventional steel building or polycarbonate/glass greenhouse construction:</p>
    <div class="benefit"><span class="benefit__icon"></span><p class="benefit__name">BUILD FASTER.</p><p class="benefit__text">At least 12 weeks faster than conventional construction of the exterior and interior structure accelerating time to first harvest</p></div>
    <div class="benefit"><span class="benefit__icon"></span><p class="benefit__name">BUILT BETTER.</p><p class="benefit__text">Deliver a fully engineered, code complaint, expandable and relocatable facility using our team of designers, manufacturers, and installers</p></div>
    <div class="benefit"><span class="benefit__icon"></span><p class="benefit__name">SUPERIOR GROW ENVIRONMENT.</p><p class="benefit__text">Full blackout-controlled environment anchored by high-performance LED lights (PPF efficacy 2.85 µmols/J)</p></div>
    <div class="benefit"><span class="benefit__icon"></span><p class="benefit__name">AIRTIGHT FACILITY.</p><p class="benefit__text">A sealed, airtight building solution critical for energy efficiency, maintaining CO2 levels and providing enhanced biosecurity.</p></div>
    <div class="benefit"><span class="benefit__icon"></span><p class="benefit__name">REDUCED ENERGY USE.</p><p class="benefit__text">Tensioned membrane structure uses less energy than traditional structure, with electricity usage being consistent throughout facility</p></div>
    <div class="benefit"><span class="benefit__icon"></span><p class="benefit__name">INCREASED PROFITS.</p><p class="benefit__text">Speed to market can generate almost $2.1 million in additional crop revenue, plus beat your licensee competitors to market</p></div>
    <div class="benefit"><span class="benefit__icon"></span><p class="benefit__name">FINANCING.</p><p class="benefit__text">Qualified growers can receive interim and long-term financing from non-traditional sources for certain components of our integrated solution</p></div>
    <div class="benefit"><span class="benefit__icon"></span><p class="benefit__name">COMMITTED TEAM.</p><p class="benefit__text">Experienced vendor-partner team engaged in the process from beginning to end to assure your facility is completed and operational in a timely manner</p></div>
  </div>

  <div class="abs cover-top"></div>
  <div class="abs cover-bar"></div>
  <h1 class="abs cover-title">When Speed To<br>Market Counts - We Deliver</h1>
  <div class="abs cover-photo" role="img" aria-label="Photo: interior of a large clear-span membrane structure under construction with lifts and crates"></div>
  <div class="abs cover-base"></div>
  <div class="abs cover-strip"></div>

  <div class="abs contact">
    <h3 class="contact__title">Contact Us</h3>
    <p class="contact__line"><span class="contact__dot"></span>info@rivenstalkworks.com</p>
    <p class="contact__line"><span class="contact__dot"></span>www.rivenstalkworks.com</p>
  </div>

  <div class="abs partners">
    <div class="partner"><span class="partner__mark"></span>Brevik</div>
    <div class="partner"><span class="partner__mark"></span>Melta-Brook</div>
    <div class="partner"><span class="partner__mark"></span>Lumaveld</div>
    <div class="partner"><span class="partner__mark"></span>Korvane Enterprises</div>
  </div>
  <p class="abs cover-url">www.rivenstalkworks.com</p>
  <div class="fold"></div>
</section>

<section class="spread spread--inner">
  <div class="abs campus" role="img" aria-label="Illustration: aerial view of a cannabis campus with numbered membrane buildings among fields"></div>
  <div class="abs campus-corner"></div>

  <div class="abs buildings">
    <h2 class="buildings__title">Brevik Interactive and Buildings</h2>
    <p class="buildings__lead">Brevik structures are the ideal solution for growers, processors and producers of cannabis products. Our versatile structures are engineered to be built virtually anywhere and are perfect for on-site processing. Designed to be relocatable, Brevik structures can be moved and repurposed as needs change, adapting to growth in your industry.</p>
    <div class="bitem bitem--wide"><span class="bitem__num">1</span><p class="bitem__name">BLACKOUT GROWING STRUCTURES</p><p class="bitem__text">Complete control over your growing environment in a large clearspan structure.</p></div>
    <div class="bitem bitem--wide"><span class="bitem__num">2</span><p class="bitem__name">GREENHOUSE GROWING STRUCTURES</p><p class="bitem__text">Brevik's specially designed, highly translucent membrane provides diffused lighting for optimal growing conditions and backed by a 10 year membrane guarantee</p></div>
    <div class="bitem bitem--wide"><span class="bitem__num">3</span><p class="bitem__name">ON-SITE COMPOSTING</p><p class="bitem__text">Avoid pests, mold and rain by composting in a Brevik Structure</p></div>
    <div class="bitem bitem--wide"><span class="bitem__num">4</span><p class="bitem__name">HEAD HOUSES</p><p class="bitem__text">Give your staff space to prepare and protect your crops during the growing process.</p></div>
    <div class="bitem bitem--wide"><span class="bitem__num">5</span><p class="bitem__name">PROCESSING FACILITIES</p><p class="bitem__text">Eliminate the need to transport crops to off-site processing facilities, eliminating damage. Brevik's clear-span design provides unimpeded space for the personnel and machinery used to dry, extract, manufacture and package your products.</p></div>
    <div class="bitem"><span class="bitem__num">6</span><p class="bitem__name">ADMINISTRATION BUILDINGS</p><p class="bitem__text">Bright spacious buildings with large windows and daylight panels provide a comfortable space for your on-site admin team</p></div>
    <div class="bitem"><span class="bitem__num">7</span><p class="bitem__name">RETAIL</p><p class="bitem__text">Provide your customers with a welcoming retail experience either on site or in convenient urban locations. Glazing walls and daylight panels will provide bright, positive shopping environments.</p></div>
    <div class="bitem"><span class="bitem__num">8</span><p class="bitem__name">HAIL SHETTERS</p><p class="bitem__text">Protect millions of dollars in crops with hail shelters</p></div>
  </div>
  <div class="abs floorplan" role="img" aria-label="Illustration: cutaway floor plan of a grow building"></div>

  <div class="abs features-bg"></div>
  <h2 class="abs features-title">Features MeltaBrook</h2>
  <p class="abs features-lead">Every business needs to run as efficiently as possible. As one of the most experienced prefabricated companies in the world, we're aware of this and understand the advantages prefabricated buildings deliver. From streamlining the building process to more effective use of space and resources, prefabricated buildings offer the perfect solution for saving time and money.</p>

  <div class="tile tile--light" style="left:388px;top:139px" role="img" aria-label="Image: modular wall panels"></div>
  <div class="tile tile--room" style="left:503px;top:139px" role="img" aria-label="Image: modular grow room cutaway"></div>
  <div class="tile tile--light" style="left:619px;top:139px" role="img" aria-label="Image: prefabricated modular building"></div>
  <div class="tile tile--sky" style="left:388px;top:218px" role="img" aria-label="Photo: elevated steel guard tower"></div>
  <div class="tile tile--rows" style="left:503px;top:218px" role="img" aria-label="Photo: drying room interior"></div>
  <div class="tile tile--sky" style="left:619px;top:218px" role="img" aria-label="Photo: prefabricated guard booth"></div>

  <div class="abs modular">
    <p>When choosing between modular construction and traditionally constructed rooms, consider that all modular construction is objectively faster and more affordable. On average you can cut construction time by half when using a modular room and building design compared to conventionally construction.</p>
    <p>All components used to construct modular rooms and buildings have already been designed and fabricated at our plant, causing:</p>
  </div>
  <div class="abs perk" style="top:382px"><span class="perk__icon"></span><span>Less disruption to your daily business<br>operations</span></div>
  <div class="abs perk" style="top:415px"><span class="perk__icon"></span><span>Less construction waste and debris</span></div>

  <div class="abs wedge"></div>
  <div class="abs base-line"></div>
  <div class="fold"></div>
</section>

</body>
</html>
```